distributor of aftermarket auto electrical components

I am after business card design for my new company called
Summit Vehicle Supplies (SVS as the acronym). I will supplying automotive wiring components, basically from battery to headlight. I will be aiming to sell in the 4wd scene and to auto electricians. i am not worried which colours are used though i would like it to be dynamic.
Updates

sorry guys, i have add a mobile and e-mail address that will need to on there as well. Sorry for theĀ inconvenience.

sorry guys i had erred on my spelling with my e-mail. i have now fixed it in the brief

Target Market(s)

4wd industry, custom cars, RV, auto electricians

Industry/Entity Type

Electrical

Requirements
Must have
• Company Name
ABN number: 71 306 548 290
Director: Derek Holloway
M 0432 718 946
E dhollo@fernwire.com.au

```html
<!DOCTYPE html>
<html lang="en">
<head>
<meta charset="utf-8">
<title>Summit Vehicle Supplies – Business Card</title>
<link rel="stylesheet" href="https://fonts.googleapis.com/css2?family=Arimo:wght@400;700&display=swap">
<style>
  :root {
    --card-white: #ffffff;
    --card-peach: #f9dcc0;
    --card-apricot: #f3b676;
    --card-orange: #ef9a45;
    --brand-orange: #e8771f;
    --text-dark: #231f20;
    --edge-grey: #b5b5b5;
  }
  html, body {
    margin: 0;
    padding: 0;
    width: 1200px;
    height: 686px;
    overflow: hidden;
    background: var(--card-white);
  }
  .business-card {
    position: relative;
    box-sizing: border-box;
    width: 1200px;
    height: 686px;
    border: 1px solid var(--edge-grey);
    background: linear-gradient(90deg,
      var(--card-white) 0%,
      var(--card-peach) 38%,
      var(--card-apricot) 72%,
      var(--card-orange) 100%);
    font-family: "Arimo", Arial, sans-serif;
    color: var(--text-dark);
  }
  .company-name {
    position: absolute;
    top: 52px;
    left: 0;
    right: 0;
    margin: 0;
    text-align: center;
    font-weight: 700;
    font-size: 76px;
    line-height: 1;
    letter-spacing: 0.5px;
    color: var(--brand-orange);
  }
  .contact-details {
    position: absolute;
    left: 29px;
    top: 436px;
    margin: 0;
    font-size: 38px;
    line-height: 48px;
    font-weight: 400;
  }
  .contact-details p { margin: 0; }
</style>
</head>
<body>
  <main class="business-card">
    <h1 class="company-name">Summit Vehicle Supplies</h1>
    <section class="contact-details">
      <p class="abn">ABN Number: 71-306-548-290</p>
      <p class="director">Director&nbsp; : Derek Holloway</p>
      <p class="mobile">Mobile No.: 0432-718-946</p>
      <p class="email">Email Add.: dhollo@fernwire.com.au</p>
    </section>
  </main>
</body>
</html>
```